Modern looking signage for dental office.

Exterior signage for passing cars
Target Market(s)
Cars passing by
Font styles to use
Sans Serif
Colors
3276b5
Requirements
Must have
- Logo
- OPEN ON SUTURDAY AND SUNDAY
- NIGHT CLINIC AVAILABLE
- PLEASE USE THE FONT TYPE IN FILE 4 UPLOADED BELOW.
- (482) 730-2964
- Modern looking

```html
<!DOCTYPE html>
<html lang="en">
<head>
<meta charset="utf-8">
<title>Summit Dental – Exterior Sign</title>
<link rel="stylesheet" href="https://fonts.googleapis.com/css2?family=Josefin+Sans:wght@300&family=Open+Sans:wght@400&family=Questrial&family=Montserrat:wght@500;700&display=swap">
<style>
  :root {
    --backdrop: #e8ecee;
    --sign-white: #f3f3f3;
    --teal: #13809f;
    --teal-deep: #0f6f93;
    --teal-glow: #23a39f;
    --ink: #505050;
    --on-teal: #ffffff;
  }
  html, body {
    margin: 0;
    width: 1200px;
    height: 1000px;
    overflow: hidden;
    background: var(--backdrop);
  }
  .sign {
    position: absolute;
    left: 50px;
    top: 161px;
    width: 1100px;
    height: 678px;
    box-shadow: 0 6px 18px rgba(0,0,0,0.18);
  }
  .brand-name { font-family: "Josefin Sans", sans-serif; font-weight: 300; fill: var(--ink); }
  .brand-tagline { font-family: "Open Sans", sans-serif; fill: var(--ink); }
  .service-title { font-family: "Montserrat", sans-serif; font-weight: 700; fill: var(--teal); }
  .service-sub { font-family: "Questrial", sans-serif; fill: var(--teal); }
  .phone-number { font-family: "Questrial", sans-serif; fill: var(--teal); }
  .hours-lead { font-family: "Montserrat", sans-serif; font-weight: 700; fill: var(--on-teal); }
  .hours-days { font-family: "Questrial", sans-serif; fill: var(--on-teal); }
</style>
</head>
<body>
  <svg class="sign" viewBox="0 0 750 462" xmlns="http://www.w3.org/2000/svg" role="img" aria-label="Summit Dental sign: night clinic available, open on Saturday and Sunday">
    <defs>
      <radialGradient id="hours-panel-fill" cx="0.5" cy="0.42" r="0.7">
        <stop offset="0" stop-color="var(--teal-glow)"/>
        <stop offset="0.55" stop-color="var(--teal)"/>
        <stop offset="1" stop-color="var(--teal-deep)"/>
      </radialGradient>
    </defs>

    <rect class="sign-face" width="750" height="462" fill="var(--sign-white)"/>
    <rect class="edge-band" width="7" height="462" fill="var(--teal)"/>
    <path class="hours-panel" d="M550,0 Q446,231 550,462 L750,462 L750,0 Z" fill="url(#hours-panel-fill)"/>

    <g class="brand">
      <circle cx="80" cy="97" r="49" fill="none" stroke="var(--ink)" stroke-width="2"/>
      <text class="brand-name" x="145" y="119" font-size="52" textLength="352" lengthAdjust="spacingAndGlyphs">SUMMIT DENTAL</text>
      <text class="brand-tagline" x="175" y="149" font-size="18.5">MODERN GENERAL DENTISTRY</text>
    </g>

    <g class="service" text-anchor="middle">
      <text class="service-title" x="260" y="250" font-size="27">NIGHT CLINIC</text>
      <text class="service-sub" x="260" y="290" font-size="28">AVAILABLE</text>
    </g>

    <g class="contact">
      <circle cx="101" cy="404" r="19" fill="none" stroke="var(--teal)" stroke-width="2.5"/>
      <path d="M96,392 l5,0 l1,6 l-3,2 q2,5 5,8 l3,-2 l5,2 l0,5 q-12,1 -17,-12 q-1,-5 1,-9 z" fill="var(--teal)"/>
      <text class="phone-number" x="136" y="417" font-size="38">(482) 730-2964</text>
    </g>

    <g class="hours" text-anchor="middle">
      <text class="hours-lead" x="625" y="181" font-size="25">Open on</text>
      <text class="hours-days" x="625" y="255" font-size="37">Saturday</text>
      <text class="hours-days" x="625" y="292" font-size="37">and</text>
      <text class="hours-days" x="625" y="330" font-size="37">Sunday</text>
    </g>
  </svg>
</body>
</html>
```